Packaging Design Project for Snack product

we are manufacturer banana chips and potato based snacks.our company name is "tangora Foods" and,looking a packaging design for our new product "Potato Twirls" under brand name " Munvolos".

we need nice colour scheme and wording on the front and back.just a little more professional looking with the wow factor to help it stand out on the shelve.

so pls find below information about the design:
Company name: Tangora Foods
Brand name : Munvolos
Product name : Potato Twirls
Flavored : Sweet & Spicy
Package Size : 40 GM and 100 GM

Target Market(s)

Retail Customers

Industry/Entity Type

It Company

Requirements
Must have
• In this design we need small visible part for display our product.

```html
<!DOCTYPE html>
<html lang="en">
<head>
<meta charset="utf-8">
<title>Tangora Foods – Potato Twirls</title>
<link rel="stylesheet" href="https://fonts.googleapis.com/css2?family=Kaushan+Script&family=Rubik+Distressed&family=Archivo+Black&family=Cousine&display=swap">
<style>
  :root {
    --stage: #d9d9d9;
    --bag-red: #e8262c;
    --bag-red-deep: #c81a22;
    --bag-blue: #3aa6d6;
    --crimp: #f0452a;
    --crimp-dark: #b8141a;
    --band-blue: #3fb8e6;
    --glow-pink: #f07a9a;
    --ink: #111111;
    --white: #ffffff;
    --chip-light: #f3dc86;
    --chip-dark: #d7b24c;
  }
  * { margin: 0; padding: 0; box-sizing: border-box; }
  html, body { width: 1200px; height: 1184px; overflow: hidden; }
  body { background: var(--stage); position: relative; }

  .pack {
    position: absolute;
    left: 294px; top: 128px;
    width: 666px; height: 893px;
    background:
      radial-gradient(ellipse 58% 20% at 58% 50%, var(--bag-blue) 0%, rgba(58,166,214,0.6) 50%, rgba(58,166,214,0) 100%),
      radial-gradient(ellipse 35% 12% at 12% 42%, rgba(58,166,214,0.7) 0%, rgba(58,166,214,0) 100%),
      linear-gradient(180deg, var(--bag-red) 0%, var(--bag-red-deep) 60%, var(--bag-red) 100%);
    overflow: hidden;
  }
  .pack__crimp {
    position: absolute; left: 0; width: 100%;
    background: repeating-linear-gradient(90deg, var(--crimp) 0 6px, var(--crimp-dark) 6px 9px);
  }
  .pack__crimp--top { top: 0; height: 22px; }
  .pack__crimp--bottom { bottom: 0; height: 33px; }

  .company-glow {
    position: absolute; left: 40px; top: 70px;
    width: 590px; height: 140px;
    border-radius: 70px;
    background: radial-gradient(ellipse at 50% 50%, rgba(240,122,154,0.75) 0%, rgba(240,122,154,0.45) 55%, rgba(240,122,154,0) 75%);
  }
  .company {
    position: absolute; top: 92px; left: 0; width: 100%;
    text-align: center;
    font-family: "Kaushan Script", cursive;
    font-size: 64px; color: var(--ink);
    line-height: 1.2;
  }

  .product-word {
    position: absolute; left: 0; width: 100%;
    text-align: center;
    font-family: "Rubik Distressed", "Archivo Black", sans-serif;
    color: var(--white);
    line-height: 1;
  }
  .product-word--first { top: 240px; font-size: 132px; letter-spacing: 2px; }
  .product-word--second { top: 550px; font-size: 128px; letter-spacing: 1px; }

  .product-window {
    position: absolute; left: 104px; top: 368px;
    width: 504px; height: 188px;
    border-radius: 48% 52% 40% 45% / 55% 50% 50% 45%;
    background: radial-gradient(ellipse at 50% 45%, var(--chip-light) 0%, var(--chip-dark) 100%);
  }

  .flavour-band {
    position: absolute; left: 14px; top: 712px;
    width: 637px; height: 100px;
    background: var(--band-blue);
    display: flex; align-items: center; justify-content: center;
  }
  .flavour-band__text {
    font-family: "Archivo Black", sans-serif;
    font-size: 64px; color: var(--ink);
    letter-spacing: 3px;
  }

  .pack-sizes {
    position: absolute; right: 16px; top: 814px;
    font-family: "Cousine", monospace;
    font-size: 31px; color: var(--white);
    letter-spacing: 1px;
  }
</style>
</head>
<body>
  <div class="pack">
    <div class="pack__crimp pack__crimp--top"></div>
    <div class="company-glow"></div>
    <div class="company">Tangora Foods</div>
    <div class="product-word product-word--first">POTATO</div>
    <div class="product-window" role="img" aria-label="Window showing the potato snacks inside the pack"></div>
    <div class="product-word product-word--second">TWIRLS</div>
    <div class="flavour-band"><span class="flavour-band__text">Sweet &amp; Spicy</span></div>
    <div class="pack-sizes">40 GM and 100 GM</div>
    <div class="pack__crimp pack__crimp--bottom"></div>
  </div>
</body>
</html>
```